Velmoro Cabinets Letter Head and Email Signature

Hi
I would love a design package for a letterhead, email signature, even update my business card if you like if you can come up with a great idea for my new high end cabinet shop. Velmoro Cabinets brings timeless craftsmanship to modern interiors, specializing in high end, custom cabinetry designed for architects and interior designers.

Target Market(s)

high end, luxury market

Industry/Entity Type

cabinet making

Requirements
Must have
• my colours of logo as the theme

```html
<!DOCTYPE html>
<html lang="en">
<head>
<meta charset="utf-8">
<title>Velmoro Cabinets Letterhead</title>
<link rel="stylesheet" href="https://fonts.googleapis.com/css2?family=Poppins:wght@400;500&display=swap">
<style>
  :root {
    --brand-green: #4b7b4a;
    --panel-grey: #e8e8e8;
    --ink: #000000;
    --paper: #ffffff;
    --text-dark: #1a1a1a;
  }
  html, body { margin: 0; padding: 0; overflow: hidden; background: var(--paper); }
  .letterhead {
    position: relative;
    width: 870px;
    height: 1200px;
    overflow: hidden;
    background: var(--paper);
    font-family: "Poppins", sans-serif;
  }
  .letterhead__shapes { position: absolute; inset: 0; width: 870px; height: 1200px; }
  .brand-name {
    position: absolute;
    left: 60px;
    top: 80px;
    margin: 0;
    font-size: 34px;
    font-weight: 500;
    color: var(--brand-green);
    letter-spacing: 0.5px;
    line-height: 1;
  }
  .contact-bar {
    position: absolute;
    top: 1125px;
    left: 0;
    width: 870px;
    height: 22px;
    font-size: 17px;
    font-weight: 400;
    color: var(--text-dark);
  }
  .contact-item {
    position: absolute;
    top: 0;
    display: flex;
    align-items: center;
    gap: 6px;
    line-height: 22px;
    white-space: nowrap;
  }
  .contact-item--phone { left: 49px; }
  .contact-item--email { left: 224px; }
  .contact-item--social { left: 556px; }
  .contact-icon { width: 20px; height: 20px; flex: none; }
</style>
</head>
<body>
<main class="letterhead">
  <svg class="letterhead__shapes" viewBox="0 0 1138 1472" preserveAspectRatio="none" aria-hidden="true">
    <!-- header -->
    <polygon class="header-panel" points="0,0 682,0 548,230 0,230" fill="var(--panel-grey)"/>
    <polygon class="header-band" points="640,99 1138,99 1138,166 602,166" fill="var(--brand-green)"/>
    <polygon class="header-rule" points="370,230 548,230 640,77 653,77 557,245 370,245" fill="var(--ink)"/>
    <!-- footer -->
    <polygon class="footer-block" points="1060,1398 1138,1398 1138,1472 1020,1472" fill="var(--ink)"/>
    <polygon class="footer-panel" points="0,1337 1082,1337 1020,1447 0,1447" fill="var(--panel-grey)"/>
    <rect class="footer-base" x="0" y="1447" width="1138" height="25" fill="var(--ink)"/>
    <polygon class="footer-rule" points="850,1447 1026,1447 1099,1319 1111,1319 1032,1459 850,1459" fill="var(--brand-green)"/>
  </svg>

  <h1 class="brand-name">Velmoro Cabinets</h1>

  <footer class="contact-bar">
    <div class="contact-item contact-item--phone">
      <svg class="contact-icon" viewBox="0 0 20 20" aria-hidden="true">
        <circle cx="10" cy="10" r="10" fill="var(--brand-green)"/>
        <path d="M7 5.5c.6-.4 1.1-.2 1.4.4l.7 1.4c.2.5 0 .9-.4 1.2l-.5.4c.5 1.2 1.4 2.1 2.6 2.6l.4-.5c.3-.4.7-.6 1.2-.4l1.4.7c.6.3.8.8.4 1.4-.6.9-1.5 1.3-2.5 1-2.6-.8-4.6-2.8-5.4-5.4-.3-1 .1-1.9.7-2.6z" fill="var(--paper)"/>
      </svg>
      <span>0412358264</span>
    </div>
    <div class="contact-item contact-item--email">
      <svg class="contact-icon" viewBox="0 0 20 20" aria-hidden="true">
        <circle cx="10" cy="10" r="10" fill="var(--brand-green)"/>
        <rect x="5" y="6.5" width="10" height="7" rx="1" fill="var(--paper)"/>
        <path d="M5.5 7.2 10 10.5l4.5-3.3" fill="none" stroke="var(--brand-green)" stroke-width="1"/>
      </svg>
      <span>info@velmorocabinets.com.au</span>
    </div>
    <div class="contact-item contact-item--social">
      <svg class="contact-icon" viewBox="0 0 20 20" aria-hidden="true">
        <circle cx="10" cy="10" r="10" fill="var(--brand-green)"/>
      </svg>
      <span>@velmoro.cabinets</span>
    </div>
  </footer>
</main>
</body>
</html>
```